Business Card Design with new logo

Dorian Pelleway 4172
E 118th St Casey, IL 62420
Cell: 217-555-0193
pellewayrestoration@mailvane.test

Classic Car Restoration Services Buy Sell Trade Consign

Dorian Pelleway 9698
Cell: 217-555-0193

```html
<!DOCTYPE html>
<html lang="en">
<head>
<meta charset="utf-8">
<title>Pelleway Restoration LLC — Business Card</title>
<link rel="stylesheet" href="https://fonts.googleapis.com/css2?family=Arimo:ital,wght@0,700;1,400&display=swap">
<style>
  :root {
    --card-black: #0a0a0a;
    --brand-red: #c8282b;
    --tagline-red: #b3262a;
    --backdrop-dark: #15110f;
    --car-red-deep: #8e1a1c;
    --car-red-bright: #cf2c2c;
  }
  * { margin: 0; padding: 0; box-sizing: border-box; }
  html, body {
    width: 1200px;
    height: 771px;
    overflow: hidden;
    background: var(--card-black);
  }
  .card {
    position: relative;
    width: 1200px;
    height: 771px;
    background: var(--card-black);
    overflow: hidden;
    font-family: "Arimo", Arial, sans-serif;
  }
  .car-photo {
    position: absolute;
    left: 685px;
    top: 0;
    width: 515px;
    height: 771px;
    background: linear-gradient(90deg, var(--backdrop-dark) 0%, #1b1513 40%, var(--car-red-deep) 68%, var(--car-red-bright) 100%);
    clip-path: polygon(0 0, 100% 0, 100% 100%, 30% 100%, 30% 63%, 0 63%);
  }
  .brand {
    position: absolute;
    left: 175px;
    top: 140px;
    width: 640px;
    display: flex;
    flex-direction: column;
    align-items: center;
    color: var(--brand-red);
    font-weight: 700;
  }
  .brand-dot {
    width: 120px;
    height: 120px;
    border-radius: 50%;
    background: var(--brand-red);
    margin-bottom: 38px;
  }
  .brand-name {
    font-size: 76px;
    line-height: 1;
    letter-spacing: 0.06em;
  }
  .brand-suffix {
    margin-top: 26px;
    font-size: 32px;
    line-height: 1;
    letter-spacing: 0.55em;
    margin-right: -0.55em;
  }
  .tagline {
    position: absolute;
    left: 0;
    width: 1000px;
    top: 618px;
    text-align: center;
    font-style: italic;
    font-weight: 400;
    font-size: 19.5px;
    color: var(--tagline-red);
  }
</style>
</head>
<body>
  <main class="card">
    <div class="car-photo" role="img" aria-label="Photo of the rear quarter and tail light of a glossy red car against a dark garage wall"></div>

    <div class="brand">
      <span class="brand-dot"></span>
      <span class="brand-name">PELLEWAY</span>
      <span class="brand-suffix">RESTORATION LLC</span>
    </div>

    <p class="tagline">Classic Car Restoration Services Buy Sell Trade Consign</p>
  </main>
</body>
</html>
```